Gift Card/voucher Design for Beauty Clinic

I need a design for a gift card I Can use in all seasons for my Aesthetic clinic. The Logo is attached. The main colors we use are white and black, we are open for new suggestions to make an friendly yet professional impression. Ideally the gift card/voucher would be foldable.
The inside should contain the following fields:

Für:

Von:

Wert

Gültigkeit

```html
<!DOCTYPE html>
<html lang="de">
<head>
<meta charset="utf-8">
<title>Gift Card – Mara Lindqvist Aesthetics</title>
<link rel="stylesheet" href="https://fonts.googleapis.com/css2?family=Almendra:wght@400;700&family=Cinzel:wght@400;600;700&display=swap">
<style>
  :root {
    --page: #ffffff;
    --ink: #0d0d12;
    --brand-red: #8a1620;
    --card-top: #8f9ba4;
    --card-mid: #b9c5cf;
    --card-light: #dfe6ec;
    --card-back: #abb8c1;
    --hair-red: #c9505c;
    --hair-pink: #e48a92;
    --skin: #d9c1bb;
  }
  * { margin: 0; padding: 0; box-sizing: border-box; }
  html, body {
    width: 1200px; height: 962px; overflow: hidden;
    background: var(--page);
  }
  .canvas { position: relative; width: 1200px; height: 962px; }

  /* Cover panel */
  .cover {
    position: absolute; left: 21px; top: 33px; width: 1160px; height: 434px;
    background: linear-gradient(180deg, var(--card-top) 0%, var(--card-mid) 55%, #aab6c0 100%);
    overflow: hidden;
  }
  .cover-photo {
    position: absolute; right: 0; top: 0; width: 600px; height: 434px;
    background:
      radial-gradient(ellipse 55% 60% at 62% 62%, var(--skin) 0%, rgba(217,193,187,0.6) 40%, rgba(217,193,187,0) 70%),
      radial-gradient(ellipse 60% 75% at 78% 45%, var(--hair-red) 0%, var(--hair-pink) 45%, rgba(228,138,146,0) 75%),
      linear-gradient(90deg, rgba(223,230,236,0) 0%, var(--card-light) 30%, #c5cfd7 100%);
  }
  .cut-line {
    position: absolute; left: 135px; top: 0; height: 434px; width: 0;
    border-left: 2px dashed var(--ink);
  }
  .scissors { position: absolute; left: 103px; top: 390px; width: 30px; height: 34px; }
  .cover-title {
    position: absolute; left: 156px; top: 60px;
    font-family: "Almendra", serif; font-weight: 400;
    font-size: 80px; line-height: 1; color: var(--ink); letter-spacing: 1px;
  }
  .cover-subtitle {
    position: absolute; left: 262px; top: 122px;
    font-family: "Cinzel", serif; font-weight: 400;
    font-size: 21px; color: var(--brand-red); letter-spacing: 0.5px;
  }

  /* Brand name block */
  .brand {
    position: absolute; text-align: center;
    font-family: "Cinzel", serif; font-weight: 600; color: var(--ink);
  }
  .brand-mark {
    display: block; width: 14px; height: 14px; margin: 0 auto 8px;
    background: var(--ink); border-radius: 50%;
  }
  .brand-name { display: block; font-size: 10px; letter-spacing: 0.6px; white-space: nowrap; }
  .brand-tag { display: block; font-size: 6px; letter-spacing: 3px; margin-top: 4px; }
  .cover .brand { left: 148px; top: 360px; width: 110px; }

  /* Inside panel */
  .inside {
    position: absolute; left: 18px; top: 489px; width: 1160px; height: 434px;
    background: var(--card-back);
  }
  .inside-title {
    position: absolute; left: 454px; top: 20px;
    font-family: "Almendra", serif; font-weight: 400;
    font-size: 54px; line-height: 1; color: var(--ink);
  }
  .inside-subtitle {
    position: absolute; left: 546px; top: 76px;
    font-family: "Cinzel", serif; font-weight: 600;
    font-size: 21px; color: var(--ink); letter-spacing: 0.5px;
  }
  .inside .brand { left: 981px; top: 30px; width: 110px; }

  .fields { position: absolute; left: 159px; top: 138px; width: 980px; }
  .field { position: relative; height: 47.5px; }
  .field-label {
    position: absolute; left: 0; top: 0;
    font-family: "Cinzel", serif; font-weight: 600;
    font-size: 20px; color: var(--ink);
  }
  .field-colon {
    position: absolute; left: 168px; top: 0;
    font-family: "Cinzel", serif; font-weight: 600; font-size: 20px; color: var(--ink);
  }
  .field-line {
    position: absolute; left: 200px; top: 21px; width: 762px; height: 0;
    border-bottom: 2.5px dotted var(--ink);
  }

  .amount { position: absolute; left: 884px; top: 340px; display: flex; gap: 7px; }
  .amount-currency {
    width: 59px; height: 55px; background: var(--ink); color: #fff;
    font-family: "Cinzel", serif; font-weight: 600; font-size: 27px;
    display: flex; align-items: center; justify-content: center;
  }
  .amount-value { width: 167px; height: 55px; background: var(--ink); }
</style>
</head>
<body>
<div class="canvas">

  <section class="cover">
    <div class="cover-photo" role="img" aria-label="Portrait photo of a woman with flowing red hair against a pale grey backdrop"></div>
    <div class="cut-line"></div>
    <svg class="scissors" viewBox="0 0 30 34" aria-hidden="true">
      <g fill="none" stroke="#0d0d12" stroke-width="1.6">
        <circle cx="7" cy="24" r="4"/>
        <circle cx="10" cy="30" r="3.5"/>
        <path d="M10 21 L26 3"/>
        <path d="M13 28 L27 12"/>
      </g>
    </svg>
    <h1 class="cover-title">Gift Card</h1>
    <p class="cover-subtitle">Aesthetic clinic</p>
    <div class="brand">
      <span class="brand-mark"></span>
      <span class="brand-name">MARA LINDQVIST</span>
      <span class="brand-tag">AESTHETICS</span>
    </div>
  </section>

  <section class="inside">
    <h2 class="inside-title">Aesthetic Beauty</h2>
    <p class="inside-subtitle">Clinic Gift Card</p>
    <div class="brand">
      <span class="brand-mark"></span>
      <span class="brand-name">MARA LINDQVIST</span>
      <span class="brand-tag">AESTHETICS</span>
    </div>

    <div class="fields">
      <div class="field"><span class="field-label">Für:</span><span class="field-colon">:</span><span class="field-line"></span></div>
      <div class="field"><span class="field-label">Von:</span><span class="field-colon">:</span><span class="field-line"></span></div>
      <div class="field"><span class="field-label">Wert</span><span class="field-colon">:</span><span class="field-line"></span></div>
      <div class="field"><span class="field-label">Gültigkeit</span><span class="field-colon">:</span><span class="field-line"></span></div>
    </div>

    <div class="amount">
      <div class="amount-currency">Rs</div>
      <div class="amount-value"></div>
    </div>
  </section>

</div>
</body>
</html>
```